Flyers needed for new business Pinebrook Haven

We have a colour and business & loyalty card currently on file, we would Ike similar colours and styles, flyers I think we make 3 folding,

Target Market(s)

We specialise in Magnesium float, infared saunas and hyperbaric oxygen chamber, all this is targeted for clients trying to manage chronic pain, weigh loss and detoxification

Industry/Entity Type

Health And Wellness

Font styles to use
Sans Serif
Decorative

Colors
33a6d7
85cae6
ffffff
9d9d9d

Requirements
Must have
• Business name an logo on front, middle I think we outline facilities and business outline, we are here to help our clients become their best selves through using our facilities we can assist them in the own journeys to becoming better able to manage chronic pain, weight loss that seems impossible to lose and provide the best meditative float experience they ever experienced
Nice to have
• Some photos of magnesium float tank, infrared sauna & oxygen chamber

```html
<!DOCTYPE html>
<html lang="en">
<head>
<meta charset="utf-8">
<title>Pinebrook Haven – Trifold Brochure</title>
<link href="https://fonts.googleapis.com/css2?family=Bebas+Neue&family=Mulish:ital,wght@0,400;0,700;1,400&display=swap" rel="stylesheet">
<style>
  :root {
    --brand-blue: #33a6d7;
    --panel-blue: #2ea3dc;
    --light-blue: #85cae6;
    --white: #ffffff;
    --grey: #9d9d9d;
    --ink: #333333;
    --page-bg: #f4f4f4;
  }
  * { box-sizing: border-box; margin: 0; padding: 0; }
  html, body { width: 1200px; height: 1000px; overflow: hidden; background: var(--page-bg); }
  body { position: relative; font-family: "Mulish", sans-serif; }

  .brochure {
    position: absolute; left: 12px; top: 76px; width: 1176px; height: 831px;
    display: flex; box-shadow: 0 2px 6px rgba(0,0,0,0.25);
  }
  .panel { position: relative; width: 392px; height: 100%; }

  /* About / services panel */
  .panel--about { background: var(--panel-blue); color: var(--white); }
  .rule { position: absolute; height: 6px; background: var(--white); width: 98px; left: 38px; }
  .heading {
    font-family: "Bebas Neue", sans-serif; font-weight: 400;
    font-size: 42px; line-height: 1; letter-spacing: 0.3px;
  }
  .panel--about .heading { position: absolute; left: 38px; }
  .about-text {
    position: absolute; left: 40px; top: 143px; width: 320px;
    font-size: 15.6px; line-height: 20.2px; text-align: justify;
  }
  .about-text strong { font-weight: 700; }
  .service-list { position: absolute; left: 39px; top: 503px; width: 321px; list-style: none; }
  .service-list li {
    display: flex; justify-content: space-between;
    font-size: 15.4px; height: 28px; line-height: 22px;
  }
  .service-list em { font-style: italic; }

  /* Contact panel */
  .panel--contact { background: var(--white); color: var(--ink); text-align: center; }
  .chat-icon { position: absolute; left: 154px; top: 50px; }
  .panel--contact .heading {
    position: absolute; top: 143px; width: 100%; font-size: 40px; color: #3a3a3a;
  }
  .intro { position: absolute; top: 191px; width: 100%; font-size: 14.6px; line-height: 19.5px; }
  .divider { position: absolute; left: 41px; top: 272px; width: 310px; height: 2px; background: #444; }
  .contact-item { position: absolute; width: 100%; font-size: 17.5px; line-height: 23px; }
  .contact-item svg { display: block; margin: 0 auto 6px; }
  .hours { position: absolute; top: 741px; width: 100%; font-style: italic; font-size: 14.6px; line-height: 19px; }
  .footer-bar { position: absolute; left: 46px; bottom: 0; width: 301px; height: 36px; background: var(--panel-blue); }

  /* Cover panel */
  .panel--cover { overflow: hidden; }
  .cover-photo {
    position: absolute; inset: 0;
    background:
      radial-gradient(ellipse at 60% 35%, rgba(60,120,160,0.55), transparent 55%),
      linear-gradient(160deg, #1d86c4 0%, #2d9fd8 45%, #1b7fbf 100%);
  }
  .brand-name {
    position: absolute; left: 38px; top: 44px;
    font-family: "Mulish", sans-serif; font-weight: 700;
    font-size: 25px; line-height: 1.1; color: var(--white); letter-spacing: 1px;
  }
  .cover-rule { position: absolute; left: 248px; top: 456px; width: 110px; height: 6px; background: var(--white); }
  .cover-headline {
    position: absolute; right: 34px; top: 480px; text-align: right;
    font-family: "Bebas Neue", sans-serif; font-size: 71px; line-height: 63px; color: var(--white);
  }
  .cover-sub {
    position: absolute; right: 34px; top: 740px; text-align: right;
    font-size: 18.5px; line-height: 24px; color: var(--white);
  }
</style>
</head>
<body>
<main class="brochure">

  <section class="panel panel--about">
    <div class="rule" style="top:56px"></div>
    <h2 class="heading" style="top:77px">About Us</h2>
    <p class="about-text"><strong>Pinebrook Haven</strong> is a detoxing wellness centre based in the beautiful Kestrel Bay area of Marlow operating for people that are on their journey to better health and overall better wellbeing. Pinebrook Haven provides a range of private facilities that are here to assist you in reducing your stresses, helping reduce your aches and pains and to help increase your body’s ability to detox and repair while providing you a more positive experience in working towards bettering your health and wellbeing.</p>

    <div class="rule" style="top:423px"></div>
    <h2 class="heading" style="top:446px">Our Services</h2>
    <ul class="service-list">
      <li><span>Foot Detox</span><span>$20.00</span></li>
      <li><span>Chromo LED Light Therapy - <em>15m</em></span><span>$30.00</span></li>
      <li><span>Chromo LED Light Therapy - <em>30m</em></span><span>$60.00</span></li>
      <li><span>Infared Sauna - <em>30m</em></span><span>$30.00</span></li>
      <li><span>Infared Sauna - <em>60m</em></span><span>$50.00</span></li>
      <li><span>Magnesium Float - <em>30m</em></span><span>$30.00</span></li>
      <li><span>Magnesium Float - <em>60m</em></span><span>$60.00</span></li>
      <li><span>Hyperbaric Chamber - <em>60m</em></span><span>$80.00</span></li>
      <li><span>Colonic Hydrotherapy - <em>60m</em></span><span>$120.00</span></li>
    </ul>
  </section>

  <section class="panel panel--contact">
    <svg class="chat-icon" width="78" height="76" viewBox="0 0 78 76" aria-hidden="true">
      <path d="M30 4 C14 4 3 14 3 27 C3 35 7 41 13 45 L9 58 L24 49 C26 50 28 50 30 50" fill="none" stroke="var(--brand-blue)" stroke-width="4.5" stroke-linejoin="round"/>
      <path d="M50 24 C64 24 75 33 75 45 C75 52 71 58 66 61 L69 73 L56 65 C54 66 52 66 50 66 C36 66 25 57 25 45 C25 33 36 24 50 24 Z" fill="var(--brand-blue)"/>
      <circle cx="40" cy="45" r="3.2" fill="#fff"/><circle cx="50" cy="45" r="3.2" fill="#fff"/><circle cx="60" cy="45" r="3.2" fill="#fff"/>
    </svg>
    <h2 class="heading">Get in Touch</h2>
    <p class="intro">Please feel free to call or email us.<br>We’d love to hear your thoughts and answer<br>any questions you may have!</p>
    <div class="divider"></div>

    <div class="contact-item" style="top:298px">
      <svg width="34" height="34" viewBox="0 0 34 34" aria-hidden="true"><circle cx="17" cy="17" r="15.5" fill="none" stroke="#333" stroke-width="2"/><path d="M11 9 L14 9 L15.5 13 L13.5 14.5 C14.5 17 16.5 19 19 20 L20.5 18 L24.5 19.5 L24.5 22.5 C24.5 24 23 25 21 24.5 C15 23 10.5 18.5 9.5 12.5 C9.2 10.5 9.8 9 11 9 Z" fill="#333"/></svg>
      0491 550 218
    </div>
    <div class="contact-item" style="top:385px">
      <svg width="34" height="34" viewBox="0 0 34 34" aria-hidden="true"><circle cx="17" cy="17" r="15.5" fill="none" stroke="#333" stroke-width="2"/><rect x="9" y="11.5" width="16" height="11" fill="none" stroke="#333" stroke-width="1.6"/><path d="M9 11.5 L17 18 L25 11.5 M9 22.5 L15 16.5 M25 22.5 L19 16.5" fill="none" stroke="#333" stroke-width="1.4"/></svg>
      hello@pinebrookhaven.com
    </div>
    <div class="contact-item" style="top:470px">
      <svg width="34" height="34" viewBox="0 0 34 34" aria-hidden="true"><circle cx="16" cy="16" r="13" fill="none" stroke="#333" stroke-width="1.8"/><ellipse cx="16" cy="16" rx="5.5" ry="13" fill="none" stroke="#333" stroke-width="1.5"/><path d="M3 16 H29 M5 9.5 H27 M5 22.5 H27" stroke="#333" stroke-width="1.5"/><path d="M22 20 L31 26 L27 27 L29.5 31.5 L27.5 32.5 L25 28 L22 31 Z" fill="#fff" stroke="#333" stroke-width="1.3"/></svg>
      www.pinebrookhaven.com
    </div>
    <div class="contact-item" style="top:556px">
      <svg width="34" height="34" viewBox="0 0 34 34" aria-hidden="true"><circle cx="17" cy="17" r="15.5" fill="none" stroke="#333" stroke-width="2"/><circle cx="17" cy="17" r="4" fill="#333"/></svg>
      social: @pinebrookhaven
    </div>
    <div class="contact-item" style="top:646px">
      <svg width="34" height="34" viewBox="0 0 34 34" aria-hidden="true"><circle cx="17" cy="17" r="15.5" fill="none" stroke="#333" stroke-width="2"/><path d="M17 26 C13 21 11 18 11 14.5 A6 6 0 0 1 23 14.5 C23 18 21 21 17 26 Z" fill="#333"/><circle cx="17" cy="14.5" r="2.2" fill="#fff"/></svg>
      14 Harbour Lane<br>Kestrel Bay Qld 4710
    </div>
    <p class="hours">Open by appointment,<br>after hours appointments available</p>
    <div class="footer-bar"></div>
  </section>

  <section class="panel panel--cover">
    <div class="cover-photo" role="img" aria-label="Photo of a woman floating relaxed on her back in bright blue water"></div>
    <div class="brand-name">Pinebrook Haven</div>
    <div class="cover-rule"></div>
    <h1 class="cover-headline">Your First<br>Step To<br>Your Better<br>Wellbeing</h1>
    <p class="cover-sub">We offer Magnesium Float and<br>Oxygen Chamber Therapies</p>
  </section>

</main>
</body>
</html>
```